Bref créative
VOREN Project
LetterHead, Business Card, Envlp
I need double sided standard sized Business Card [3.5" x 2"]
no certain font requested.
Simple
Serkan OZDIL
Business Development Specialst
Çınarlı Caddesi, Gülbahar Sokak
Korutan İş Merkezi No: 7/214
Kadıköy, İstanbul, Türkiye
so@voren.com.tr
www.voren.com.tr
up to designer
Please use the attached file , all u need is there

```html
<!DOCTYPE html>
<html lang="en">
<head>
<meta charset="utf-8">
<title>VOREN Project – Stationery</title>
<link href="https://fonts.googleapis.com/css2?family=Open+Sans:wght@300;400;600&display=swap" rel="stylesheet">
<style>
:root{
  --bg:#d9dcdf;
  --paper:#ffffff;
  --blue:#1f63c4;
  --blue-dark:#0b3a8a;
  --blue-light:#4f8fe0;
  --tile:#e6e6f0;
  --ink:#3d3d46;
  --ink-soft:#85858f;
}
*{box-sizing:border-box;margin:0;padding:0}
html,body{width:1200px;height:871px;overflow:hidden}
body{background:var(--bg);font-family:"Open Sans",sans-serif;color:var(--ink);position:relative}

.sheet{position:absolute;background:var(--paper);box-shadow:0 4px 14px rgba(0,0,0,.18);overflow:hidden}

.brand{display:flex;align-items:center;gap:8px;color:var(--blue);font-weight:400;letter-spacing:2px;white-space:nowrap}
.brand-dot{display:inline-block;border-radius:50%;background:var(--blue)}

.tile{position:absolute;background:var(--tile);border-radius:22%}

/* business card */
.card{left:40px;top:40px;width:350px;height:200px}
.card .brand{position:absolute;left:24px;top:26px;font-size:22px}
.card .brand-dot{width:20px;height:20px}
.card .tile-a{right:22px;top:20px;width:40px;height:40px}
.card .tile-b{right:70px;top:44px;width:30px;height:30px}
.card .rule{position:absolute;left:24px;right:22px;top:102px;height:1px;background:var(--blue)}
.card-person{position:absolute;right:22px;top:110px;text-align:right}
.card-name{font-size:14px;font-weight:600;color:var(--blue);line-height:1.3}
.card-role{font-size:9.5px;color:var(--ink-soft)}
.card-contact{position:absolute;left:24px;top:150px;font-size:9.5px;line-height:1.5;color:var(--ink-soft)}

/* envelope */
.envelope{left:40px;top:300px;width:560px;height:420px}
.envelope .brand{position:absolute;left:28px;top:28px;font-size:24px}
.envelope .brand-dot{width:22px;height:22px}
.return-address{position:absolute;left:28px;top:72px;font-size:9.5px;line-height:1.6;color:var(--ink-soft)}
.envelope .tile-a{right:30px;top:24px;width:48px;height:48px}
.envelope .tile-b{right:92px;top:24px;width:36px;height:36px}
.envelope-band{position:absolute;left:0;right:0;bottom:0;height:80px;
  background:linear-gradient(90deg,var(--blue-dark),var(--blue) 55%,var(--blue-light))}

/* letterhead */
.letterhead{left:624px;top:30px;width:550px;height:810px}
.letterhead .brand{position:absolute;left:34px;top:34px;font-size:24px}
.letterhead .brand-dot{width:22px;height:22px}
.head-rule{position:absolute;left:150px;right:80px;top:80px;height:1px;background:var(--blue)}
.side-band{position:absolute;right:0;top:0;width:64px;height:300px;
  background:linear-gradient(180deg,var(--blue-light),var(--blue) 45%,var(--blue-dark));
  display:flex;justify-content:center;padding-top:30px}
.side-band .brand-dot{width:30px;height:30px;background:#fff}
.letterhead .tile-a{right:90px;top:380px;width:42px;height:42px}
.letterhead .tile-b{right:100px;top:450px;width:36px;height:36px}
.letterhead .tile-c{right:140px;top:500px;width:46px;height:46px}

.letter{position:absolute;left:60px;top:130px;width:330px;font-size:10px;line-height:1.65;color:var(--ink)}
.letter p{margin-bottom:12px}
.letter .date{color:var(--ink-soft)}
.signoff{margin-top:20px}
.signature{display:block;width:60px;height:22px;margin:6px 0}
.signer{font-weight:600;color:var(--blue)}
.letter-foot{position:absolute;left:34px;right:34px;bottom:26px;border-top:1px solid var(--blue);padding-top:8px;
  font-size:8.5px;line-height:1.6;color:var(--ink-soft);text-align:right}
.letter-foot span{display:block;white-space:nowrap}
</style>
</head>
<body>

<section class="sheet card" aria-label="Business card">
  <div class="brand"><span class="brand-dot"></span>VOREN</div>
  <span class="tile tile-a"></span><span class="tile tile-b"></span>
  <div class="rule"></div>
  <div class="card-person">
    <div class="card-name">Serkan OZDIL</div>
    <div class="card-role">Business Development Specialist</div>
  </div>
  <div class="card-contact">
    Çınarlı Caddesi, Gülbahar Sokak<br>
    Korutan İş Merkezi No: 7/214, Kadıköy, İstanbul<br>
    so@voren.com.tr · www.voren.com.tr
  </div>
</section>

<section class="sheet envelope" aria-label="Envelope">
  <div class="brand"><span class="brand-dot"></span>VOREN</div>
  <div class="return-address">
    Çınarlı Caddesi, Gülbahar Sokak<br>
    Korutan İş Merkezi No: 7/214<br>
    Kadıköy, İstanbul, Türkiye
  </div>
  <span class="tile tile-a"></span><span class="tile tile-b"></span>
  <div class="envelope-band"></div>
</section>

<section class="sheet letterhead" aria-label="Letterhead">
  <div class="brand"><span class="brand-dot"></span>VOREN</div>
  <div class="head-rule"></div>
  <div class="side-band"><span class="brand-dot"></span></div>
  <span class="tile tile-a"></span><span class="tile tile-b"></span><span class="tile tile-c"></span>

  <div class="letter">
    <p class="date">12 March 2024</p>
    <p>Recipient Name<br>Company Name<br>Street Address 12<br>City, Country</p>
    <p>Dear Sir or Madam,</p>
    <p>Thank you for your interest in our services. We are pleased to share the details of our project plan and look forward to working together.</p>
    <p>Please find the attached documents with the proposed schedule and budget. Do not hesitate to contact us with any questions.</p>
    <p>We value our partnership and remain at your service.</p>
    <div class="signoff">
      Sincerely,
      <svg class="signature" viewBox="0 0 60 22" aria-hidden="true">
        <path d="M2 16 C10 2,14 22,22 10 S34 4,38 14 S50 8,58 6" fill="none" stroke="var(--ink)" stroke-width="1.2"/>
      </svg>
      <span class="signer">Serkan OZDIL</span><br>
      Business Development Specialist
    </div>
  </div>

  <div class="letter-foot">
    <span>Çınarlı Caddesi, Gülbahar Sokak · Korutan İş Merkezi No: 7/214 · Kadıköy, İstanbul, Türkiye</span>
    <span>so@voren.com.tr · www.voren.com.tr</span>
  </div>
</section>

</body>
</html>
```